Accounting Practice Business Card Design

I have a logo I am happy for you to use in the design of the Business Card.
You can edit and change colours as you please, I am not fixated on it.
I am looking for a modern and clean overall feel for the finished design.

The business is a small accounting practice who thrives on word of mouth referrals and this card will be given to all current and prospect clients.

Industry/Entity Type

Accountant

Contact Information for Business Card

Marcus Elwin
Level 5, 8 Corvale Ridge Road
ASHGROVE RISE VIC 3187
Phone: 9481 3057
Email: melwin@mrfaccountants.com.au
Web: www.mrfaccountants.com.au

Font styles to use
Serif
Sans Serif

Colors
0555a3
3277b5
85acd3
0393ce
33a6d7
85cae6
00a990
33b8a4
9bcb3c

Requirements
Must have
• "The end to your tax problems begin with us"
• "A referral from you is our greatest compliment"
Nice to have
• Modern clean professional

```html
<!DOCTYPE html>
<html lang="en">
<head>
<meta charset="utf-8">
<title>MRF Accountants – Business Card</title>
<link rel="stylesheet" href="https://fonts.googleapis.com/css2?family=Lato:wght@300;400;700;900&display=swap">
<style>
  :root {
    --stage: #3a3d42;
    --sky: #35a4d7;
    --blue: #0393ce;
    --teal: #33b8a4;
    --white: #ffffff;
    --ink: #4a4d52;
    --rule: #9a9ea3;
    --rule-light: rgba(255,255,255,0.55);
  }
  * { box-sizing: border-box; margin: 0; padding: 0; }
  html, body { width: 1200px; height: 1200px; overflow: hidden; }
  body {
    background: var(--stage);
    font-family: "Lato", Arial, sans-serif;
    position: relative;
  }
  .card {
    position: absolute;
    left: 150px;
    width: 900px;
    height: 514px;
    border-radius: 38px;
    overflow: hidden;
  }
  /* Front: referral side */
  .card--front { top: 50px; background: var(--sky); color: var(--white); }
  .front__brand {
    position: absolute; left: 0; right: 0; top: 110px;
    text-align: center;
  }
  .front__brand-name {
    font-weight: 900; font-size: 64px; letter-spacing: 4px; line-height: 1;
  }
  .front__brand-sub {
    font-weight: 900; font-size: 30px; letter-spacing: 9px; margin-top: 12px;
  }
  .front__referral {
    position: absolute; left: 0; right: 0; top: 278px;
    text-align: center; font-weight: 400; font-size: 19px; letter-spacing: 5px;
  }
  .front__thanks {
    position: absolute; left: 0; right: 0; top: 322px;
    display: flex; align-items: center; justify-content: center; gap: 22px;
  }
  .front__thanks-rule { flex: 0 0 220px; height: 1px; background: var(--rule-light); }
  .front__thanks-text { text-align: center; font-size: 18px; line-height: 1.35; }
  .front__thanks-text strong { display: block; font-weight: 700; }
  .front__base-rule {
    position: absolute; left: 60px; right: 60px; bottom: 70px;
    height: 1px; background: var(--rule-light);
  }

  /* Back: contact side */
  .card--back { top: 636px; background: var(--white); color: var(--ink); }
  .back__person {
    position: absolute; right: 70px; top: 52px; text-align: right;
  }
  .back__name { color: var(--blue); font-weight: 900; font-size: 38px; line-height: 1.1; }
  .back__role { font-weight: 400; font-size: 21px; margin-top: 4px; }
  .back__divider {
    position: absolute; left: 0; right: 60px; top: 232px; height: 1px; background: var(--rule);
  }
  .back__brand {
    position: absolute; left: 70px; top: 178px;
    background: var(--white); padding: 0 18px;
    color: var(--blue); font-weight: 900; line-height: 1;
  }
  .back__brand-name { font-size: 60px; letter-spacing: 3px; }
  .back__brand-sub { font-size: 24px; letter-spacing: 7px; margin-top: 10px; }
  .back__tagline {
    position: absolute; right: 70px; top: 198px;
    color: var(--blue); font-size: 20px; font-weight: 400;
  }
  .back__contacts {
    position: absolute; right: 60px; top: 286px;
    list-style: none; text-align: right; font-size: 21px; line-height: 1.55;
  }
  .back__contacts li { display: flex; align-items: center; justify-content: flex-end; gap: 10px; }
  .back__contacts svg { width: 18px; height: 18px; flex: none; }
  .back__address {
    position: absolute; left: 70px; top: 360px;
    display: flex; align-items: center; gap: 12px;
    font-size: 20px; line-height: 1.3;
  }
  .back__address svg { width: 20px; height: 26px; flex: none; }
  .back__band { position: absolute; left: 0; bottom: 0; width: 900px; height: 60px; }
</style>
</head>
<body>

<section class="card card--front" aria-label="Card front">
  <div class="front__brand">
    <div class="front__brand-name">MRF</div>
    <div class="front__brand-sub">ACCOUNTANTS</div>
  </div>
  <p class="front__referral">A referral from you is our greatest compliment.</p>
  <div class="front__thanks">
    <span class="front__thanks-rule"></span>
    <p class="front__thanks-text">Thank you for choosing us.<strong>MRF Accountants</strong></p>
    <span class="front__thanks-rule"></span>
  </div>
  <span class="front__base-rule"></span>
</section>

<section class="card card--back" aria-label="Card back">
  <div class="back__person">
    <div class="back__name">Marcus Elwin</div>
    <div class="back__role">Accountant</div>
  </div>

  <span class="back__divider"></span>
  <div class="back__brand">
    <div class="back__brand-name">MRF</div>
    <div class="back__brand-sub">ACCOUNTANTS</div>
  </div>
  <p class="back__tagline">The end to your tax problems begin with us.</p>

  <ul class="back__contacts">
    <li>9481 3057
      <svg viewBox="0 0 20 20"><rect width="20" height="20" rx="4" fill="var(--blue)"/><path d="M6 4.5l2 .2 1 3-1.4 1a7 7 0 0 0 3.7 3.7l1-1.4 3 1 .2 2c-.2 1-1 1.5-2 1.5A10 10 0 0 1 4.5 6.5c0-1 .5-1.8 1.5-2z" fill="#fff"/></svg>
    </li>
    <li>melwin@mrfaccountants.com.au
      <svg viewBox="0 0 20 20"><rect x="1" y="4" width="18" height="12" rx="1.5" fill="var(--blue)"/><path d="M1.5 5l8.5 6.5L18.5 5" fill="none" stroke="#fff" stroke-width="1.4"/></svg>
    </li>
    <li>www.mrfaccountants.com.au
      <svg viewBox="0 0 20 20" fill="none" stroke="var(--blue)" stroke-width="1.4"><circle cx="10" cy="10" r="8"/><ellipse cx="10" cy="10" rx="3.5" ry="8"/><path d="M2 10h16M3.5 6h13M3.5 14h13"/></svg>
    </li>
  </ul>

  <div class="back__address">
    <svg viewBox="0 0 20 26"><path d="M10 1a7 7 0 0 0-7 7c0 5 7 12 7 12s7-7 7-12a7 7 0 0 0-7-7z" fill="none" stroke="var(--blue)" stroke-width="2"/><circle cx="10" cy="8" r="2.6" fill="var(--blue)"/><path d="M2 24h16" stroke="var(--blue)" stroke-width="2"/></svg>
    <p>Level 5, 8 Corvale Ridge Road<br>ASHGROVE RISE VIC 3187</p>
  </div>

  <svg class="back__band" viewBox="0 0 900 60" preserveAspectRatio="none" aria-hidden="true">
    <polygon points="0,38 500,38 540,60 0,60" fill="var(--teal)"/>
    <polygon points="520,22 900,22 900,60 566,60" fill="var(--sky)"/>
  </svg>
</section>

</body>
</html>
```